TALLOWIN COMPANY - GYM EQUIPMENT FLYER NEEDED!

Hello creative minds!

We're in need of a flyer for our fitness equipment. This flyer will be focused on 1 machine and the details surrounding the accessories, customization and function. Please be creative, there's lots of text so if you can put an image, logo or icon in it's place please do so! (I've attached a terrible draft for a rough guideline)

Name: Tallowin Company (Font: Grizzly Attack)
Website: tallowinco.com.au
(All other text can be: Abel Google Fonts)

Feel and look (Choose between 2totally different styles)

1. Design can be inspired by rustic, earthy, wood, tree - jungle feel that's clean or mystical. If you're more inclined to do this type of flyer go to www.tallowinco.com.au to see the page and feel. To gain access to the site password is: moputo

2. 90's inspired that feels like the arcade games (Pixel Rumble, Cosmic Pickle Pirate Badgers etc), 90's action movie posters and colours that pop like 90's Fizzlewhirl (purples, blues, reds and all the colours of the neon rainbow)

Go nuts with creativity or be clean and minimalist with a down to earth feel. It's entirely up to you!

All the best & feel free to shoot off with the questions!

```html
<!DOCTYPE html>
<html lang="en">
<head>
<meta charset="utf-8">
<title>Tallowin Company – Pre Order Flyer</title>
<link rel="stylesheet" href="https://fonts.googleapis.com/css2?family=Abel&family=Barlow+Semi+Condensed:wght@600;700&family=Oswald:wght@600&family=Open+Sans:wght@700&display=swap">
<style>
  :root {
    --page: #ececec;
    --forest-deep: #0f3a2b;
    --forest-mid: #1a5e42;
    --white: #ffffff;
    --signal-yellow: #fff200;
    --heading-yellow: #f3ef4a;
    --swatch-black: #000000;
    --swatch-red: #e8141c;
    --badge-red: #b01e22;
    --badge-ring: #f5e04a;
    --ink: #111111;
    --machine-dark: #1b1f1d;
  }
  * { margin: 0; padding: 0; box-sizing: border-box; }
  html, body { width: 698px; height: 1200px; overflow: hidden; background: var(--page); }
  .flyer {
    position: absolute; left: 0; top: 106px; width: 698px; height: 987px; overflow: hidden;
    background:
      radial-gradient(ellipse 260px 330px at 500px 560px, rgba(60,190,120,.5), transparent 70%),
      repeating-linear-gradient(90deg, rgba(0,0,0,.08) 0 6px, transparent 6px 19px, rgba(255,255,255,.03) 19px 23px, transparent 23px 41px),
      linear-gradient(180deg, var(--forest-deep) 0%, #154a37 30%, var(--forest-mid) 55%, #1f6b49 75%, #195639 100%);
    box-shadow: 0 6px 18px rgba(0,0,0,.35);
    font-family: "Abel", sans-serif; color: var(--white);
  }
  .flyer > * { position: absolute; }
  .brand-name { left: 0; width: 100%; top: 48px; text-align: center; font-size: 62px; font-weight: 400; letter-spacing: 2px; line-height: 1; }
  .brand-tagline { left: 0; width: 100%; top: 118px; text-align: center; font-size: 36px; letter-spacing: 2px; line-height: 1; }
  .label { font-size: 25px; line-height: 1; letter-spacing: .3px; }
  .colour-label { left: 30px; top: 222px; }
  .gift-label { left: 347px; top: 212px; font-size: 29px; }
  .swatch { width: 40px; height: 40px; border-radius: 50%; top: 250px; }
  .swatch--yellow { left: 28px; background: var(--signal-yellow); }
  .swatch--black { left: 80px; background: var(--swatch-black); }
  .swatch--red { left: 133px; background: var(--swatch-red); }
  .gift-option { left: 350px; width: 273px; height: 31px; background: var(--signal-yellow); color: var(--ink); font-size: 25px; line-height: 31px; padding-left: 3px; }
  .gift-option--bench { top: 251px; }
  .gift-option--plates { top: 290px; }
  .section-heading { font-family: "Barlow Semi Condensed", sans-serif; font-weight: 600; color: var(--heading-yellow); font-size: 26px; line-height: 1; letter-spacing: .3px; }
  .section-heading::after { content: ""; position: absolute; left: 0; bottom: -9px; height: 1px; background: rgba(255,255,255,.75); width: var(--rule, 80px); }
  .features-heading { left: 30px; top: 314px; --rule: 80px; }
  .accessories-heading { left: 30px; top: 522px; --rule: 156px; }
  .custom-heading { left: 30px; top: 717px; }
  .custom-heading::after { display: none; }
  .dimensions-heading { left: 331px; top: 818px; font-size: 29px; --rule: 160px; }
  .checklist { left: 30px; list-style: none; font-size: 15.5px; line-height: 21px; }
  .checklist li { display: flex; align-items: center; gap: 9px; }
  .checklist svg { width: 12px; height: 10px; flex: none; }
  .features-list { top: 354px; }
  .accessories-list { top: 569px; }
  .machine-image { left: 318px; top: 352px; width: 352px; height: 445px;
    background: linear-gradient(160deg, rgba(27,31,29,.85) 0%, rgba(27,31,29,.7) 55%, rgba(27,31,29,.45) 100%); }
  .preorder-badge { left: 27px; top: 759px; width: 150px; height: 150px; border-radius: 50%; background: var(--badge-red);
    border: 4px solid var(--white); box-shadow: inset 0 0 0 3px var(--badge-ring), 0 2px 4px rgba(0,0,0,.4);
    display: flex; flex-direction: column; align-items: center; justify-content: center;
    font-family: "Oswald", sans-serif; font-weight: 600; font-size: 36px; line-height: 1.02; }
  .now-badge { left: 167px; top: 791px; width: 86px; height: 86px; border-radius: 50%; background: var(--heading-yellow); color: var(--ink);
    display: flex; align-items: center; justify-content: center; padding-left: 6px; font-family: "Barlow Semi Condensed", sans-serif; font-weight: 700; font-size: 24px; }
  .dimensions { left: 331px; top: 869px; display: flex; align-items: center; gap: 5px; font-size: 26px; line-height: 1; }
  .dim-key { background: var(--heading-yellow); color: var(--ink); font-size: 22px; padding: 2px 3px; line-height: 1; }
  .dim-value { margin-right: 5px; }
  .website { right: 27px; top: 918px; font-family: "Open Sans", sans-serif; font-weight: 700; font-size: 33px; letter-spacing: 3px; line-height: 1; }
</style>
</head>
<body>
<main class="flyer">
  <h1 class="brand-name">TALLOWIN COMPANY</h1>
  <p class="brand-tagline">TRAIN LIKE A TITAN</p>

  <p class="label colour-label">CHOOSE YOUR COLOUR</p>
  <span class="swatch swatch--yellow" aria-label="Yellow"></span>
  <span class="swatch swatch--black" aria-label="Black"></span>
  <span class="swatch swatch--red" aria-label="Red"></span>

  <p class="label gift-label">CHOOSE YOUR FREE GIFT</p>
  <p class="gift-option gift-option--bench">Commercial bench</p>
  <p class="gift-option gift-option--plates">150kgs worth of plates</p>

  <h2 class="section-heading features-heading">Features:</h2>
  <ul class="checklist features-list">
    <li><svg viewBox="0 0 12 10"><path d="M1 5l3.5 3.5L11 1.5" fill="none" stroke="#fff" stroke-width="2"/></svg>Multi-grip chin up bar</li>
    <li><svg viewBox="0 0 12 10"><path d="M1 5l3.5 3.5L11 1.5" fill="none" stroke="#fff" stroke-width="2"/></svg>Power Rack</li>
    <li><svg viewBox="0 0 12 10"><path d="M1 5l3.5 3.5L11 1.5" fill="none" stroke="#fff" stroke-width="2"/></svg>Smith Machine</li>
    <li><svg viewBox="0 0 12 10"><path d="M1 5l3.5 3.5L11 1.5" fill="none" stroke="#fff" stroke-width="2"/></svg>Cable Crossover</li>
    <li><svg viewBox="0 0 12 10"><path d="M1 5l3.5 3.5L11 1.5" fill="none" stroke="#fff" stroke-width="2"/></svg>suspension trainer ring compatible</li>
    <li><svg viewBox="0 0 12 10"><path d="M1 5l3.5 3.5L11 1.5" fill="none" stroke="#fff" stroke-width="2"/></svg>6x Olympic sized weight plate holders</li>
    <li><svg viewBox="0 0 12 10"><path d="M1 5l3.5 3.5L11 1.5" fill="none" stroke="#fff" stroke-width="2"/></svg>Dual 80KG Weight stack</li>
  </ul>

  <h2 class="section-heading accessories-heading">Included accessories:</h2>
  <ul class="checklist accessories-list">
    <li><svg viewBox="0 0 12 10"><path d="M1 5l3.5 3.5L11 1.5" fill="none" stroke="#fff" stroke-width="2"/></svg>Core Trainer</li>
    <li><svg viewBox="0 0 12 10"><path d="M1 5l3.5 3.5L11 1.5" fill="none" stroke="#fff" stroke-width="2"/></svg>Lat Pull Down Bar</li>
    <li><svg viewBox="0 0 12 10"><path d="M1 5l3.5 3.5L11 1.5" fill="none" stroke="#fff" stroke-width="2"/></svg>T-Bar</li>
    <li><svg viewBox="0 0 12 10"><path d="M1 5l3.5 3.5L11 1.5" fill="none" stroke="#fff" stroke-width="2"/></svg>Olympic Lock Collars</li>
    <li><svg viewBox="0 0 12 10"><path d="M1 5l3.5 3.5L11 1.5" fill="none" stroke="#fff" stroke-width="2"/></svg>Multi-Grip Dip Handles</li>
    <li><svg viewBox="0 0 12 10"><path d="M1 5l3.5 3.5L11 1.5" fill="none" stroke="#fff" stroke-width="2"/></svg>safety Arms</li>
  </ul>

  <h2 class="section-heading custom-heading">Custom Built Order</h2>

  <div class="machine-image" role="img" aria-label="Product photo of the black multi-function power rack with Smith machine, cable crossover and weight stacks"></div>

  <div class="now-badge">NOW!</div>
  <div class="preorder-badge"><span>PRE</span><span>ORDER</span></div>

  <h2 class="section-heading dimensions-heading">Assembled Dimensions:</h2>
  <p class="dimensions">
    <span class="dim-key">D</span><span class="dim-value">145cm</span>
    <span class="dim-key">W</span><span class="dim-value">220cm</span>
    <span class="dim-key">H</span><span>247cm</span>
  </p>

  <p class="website">www.tallowinco.com.au</p>
</main>
</body>
</html>
```